Wordpress Design For Financial Investment Company

//** NEW WIREFRAME ADDED TO HELP WITH LAYOUT ISSUES. PLEASE REFER TO WIREFRAME IN ATTACHED FILES. NO DESIGN WILL BE CONSIDERED IF IT DOES NOT FOLLOW THE WIREFRAME. **//
//** PLEASE READ THE ENTIRE BRIEF INCLUDING ALL UPDATES TO THE BRIEF. THE CLIENT IS VERY SPECIFIC ABOUT WHAT THEY WANT AND I'VE COVERED SEVERAL THINGS IN THE UPDATES. THERE IS ALSO A VIDEO UPDATE THAT HAS SOME VALUABLE INFORMATION IN IT FOR THIS CONTEST. **//
The client is an investment advisor who needs a new website designed. The current site is http://www.velmorfield.net.
The client wants the site to be green to match the attached logo.
The home page should have relevant images in the rotator. No people hugging! This is a financial investment site, not a family counseling site.
Also, the client wants 4 buttons on the home page to highlight the 4 main areas they focus on:
Investment Advice and Education
General Financial Planning
Retirement Planning
401K Planning
The top right area of the site needs to have their phone number, a call to action, and 2 buttons.
Their phone number is 303-418-7639
The call to action should say something like "Call for a free consultation!"
The buttons need to say:
Login To Your Bluvexa Account
Login To Your Quillbrook Account
The final design should communicate professionalism, financial safety and growth.
Main navigation should be:
Home
About Us
Associates
Services
Contact
Mission Statement (Could also be "Our Mission")
This is a site that the client likes: http://www.pwkinvestmentconsulting.com/
Updates
The designs should not have:
Newsletter content. A newsletter sign up is fine
Learning Center
Calculators
Stock prices/tickers
The design should have a contact form on the page.
I have talked to my client and have some updates. I did a video update because I thought it would be easier to show what I'm trying to get across.
Reason: I am going to be extending the contest a few more days. I'm still not getting quite what I want and very few people are even trying to follow the creative brief and the updates to it.
PLEASE read the entire brief and the updates. There is also a video I made that explains everything. I've also attached a wireframe.
Thanks!
Target Market(s)
People looking for a high-end financial investment company.
Industry/Entity Type
Investment
Requirements
Must have
- !!FOLLOW THE WIREFRAME FOR LAYOUT!!
!!THEIR LOGO!!
4 buttons to highlight their main practice areas
Phone number in the top right
"Free Consultation" call to action
2 Login buttons in the top right
A contact form on the page.
Should not have
- The designs should not have:
Learning Center
Calculators
Stock prices/tickers

```html
<!DOCTYPE html>
<html lang="en">
<head>
<meta charset="utf-8">
<title>Velmorfield Financial</title>
<link rel="stylesheet" href="https://fonts.googleapis.com/css2?family=Open+Sans:ital,wght@0,400;0,600;0,700;1,400&family=PT+Sans+Narrow:wght@400;700&display=swap">
<style>
:root{
  --page:#eef1f2;
  --dark:#262a2a;
  --dark-2:#343a3a;
  --green:#3f6b64;
  --green-light:#5d8a82;
  --teal:#2f8f8a;
  --text:#555;
  --heading:#3a3a3a;
  --panel:#ededed;
  --line:#d9dcdc;
}
*{box-sizing:border-box;margin:0;padding:0}
html,body{width:942px;height:1200px;overflow:hidden;background:var(--page)}
body{font-family:"Open Sans",sans-serif;color:var(--text)}
.stage{position:relative;width:1178px;height:1500px;transform:scale(.8);transform-origin:0 0}
.abs{position:absolute}
.narrow{font-family:"PT Sans Narrow",sans-serif}
.sheet{position:absolute;left:128px;top:0;width:920px;height:1476px;background:#fff}

/* nav */
.topnav{left:128px;top:0;width:920px;height:50px;background:linear-gradient(#353a3a,#232626)}
.topnav a{position:absolute;top:17px;font-size:13px;color:#e6e6e6;text-decoration:none;letter-spacing:.3px}
.topnav a.current{color:#4fb3aa}
.search{position:absolute;left:727px;top:13px;width:158px;height:24px;background:#fff;border:1px solid #ccc;font-size:10px;font-style:italic;color:#4a89b5;padding:5px 9px}

/* header */
.band{left:128px;top:88px;width:920px;height:50px;background:linear-gradient(90deg,#3d6a62,#5b8a80 50%,#3d6a62);border-top:1px solid #9bb;border-bottom:1px solid #9bb}
.tagline{left:304px;top:104px;font-size:16px;font-style:italic;color:#fff;letter-spacing:.4px}
.brand{left:166px;top:94px;width:126px;font-family:"PT Sans Narrow",sans-serif;font-weight:700;font-size:17px;line-height:19px;color:#fff;letter-spacing:.5px}
.callbox{left:715px;top:52px;width:313px;height:114px;background:#fff;box-shadow:0 2px 8px rgba(0,0,0,.25);text-align:center}
.callbox .cta{margin-top:16px;font-size:13px;font-weight:700;letter-spacing:1px;color:#2b2b2b}
.callbox .phone{font-size:36px;font-weight:700;color:var(--green);line-height:1;letter-spacing:1px}
.login{position:absolute;top:72px;height:28px;background:var(--dark);color:#fff;font-size:13px;line-height:28px;padding:0 7px;border:1px solid #111}

/* hero */
.hero{left:165px;top:177px;width:849px;height:304px;background:linear-gradient(180deg,#2c63a8 0%,#8fb0d6 35%,#9ab07a 55%,#7a9a3a 70%,#5f5a52 100%)}
.hero-card{left:671px;top:240px;width:314px;height:180px;background:rgba(50,56,56,.82)}
.hero-card h1{position:absolute;left:22px;top:14px;font-size:26px;font-weight:700;color:#fff;line-height:1.12}
.hero-card p{position:absolute;left:22px;top:82px;width:290px;font-size:13.5px;color:#fff;line-height:1.5}
.hero-btn{position:absolute;left:23px;top:130px;width:268px;height:34px;background:#eee;color:#2b2b2b;font-size:15px;letter-spacing:.8px;text-align:center;line-height:34px}

/* intro */
.intro-bar{left:165px;top:502px;width:6px;height:133px;background:var(--green)}
.intro h2{position:absolute;left:190px;top:506px;font-size:18px;font-weight:700;letter-spacing:1px;color:var(--heading)}
.intro p{position:absolute;left:190px;top:535px;width:560px;font-size:12px;line-height:21.5px;letter-spacing:.4px}
.intro a{color:var(--teal);text-decoration:none}
.more-link{position:absolute;left:189px;top:614px;font-size:10px;font-weight:700;letter-spacing:1px;color:#333}
.news-box{left:778px;top:502px;width:236px;height:136px;border:1px solid var(--line)}
.news-box .head{height:27px;background:var(--green);color:#fff;text-align:center;font-size:16px;line-height:27px}
.field{position:absolute;left:15px;width:206px;height:25px;border:1px solid #ccc;font-size:10px;font-style:italic;color:#999;padding:6px 10px}
.btn{position:absolute;background:var(--dark);color:#fff;font-family:"PT Sans Narrow",sans-serif;font-size:13px;text-align:center;line-height:24px;height:24px}

.dots{left:162px;width:852px;border-top:2px dotted #c8cccc}

/* cards */
.card{position:absolute;top:686px;width:204px;height:247px;border:1px solid var(--line);text-align:center}
.card .head{height:28px;background:var(--green);color:#fff;font-size:16px;line-height:28px}
.card .pic{height:87px}
.card h3{font-size:11.5px;font-weight:700;color:#333;margin-top:9px;letter-spacing:.3px}
.card p{font-size:11.5px;line-height:21px;margin-top:1px;letter-spacing:.3px}
.card .btn{left:72px;top:212px;width:62px}

/* lower */
.col-title{position:absolute;font-size:18px;font-weight:700;letter-spacing:1.2px;color:var(--heading)}
.news{position:absolute;left:158px;width:269px;background:var(--panel);padding:5px 6px;font-size:11px;line-height:16px;letter-spacing:.3px}
.news a{color:var(--teal);font-size:12px;text-decoration:underline}
.news .date{color:#333;margin-top:3px}
.news em{color:var(--teal);font-size:10px}
.qlinks{position:absolute;left:480px;top:1016px;list-style:none}
.qlinks li{height:31.6px;font-size:13px;letter-spacing:.6px}
.qlinks a{color:var(--teal);margin-left:15px;text-decoration:underline}
.qlinks svg{vertical-align:-1px}
.event{position:absolute;left:750px;width:270px}
.event .thumb{position:absolute;left:0;top:0;width:74px;height:74px;border:3px solid #fff;box-shadow:0 0 3px rgba(0,0,0,.35)}
.event .txt{position:absolute;left:80px;top:-2px;font-size:11.5px;line-height:16px;letter-spacing:.4px}
.event .d{color:var(--teal);font-size:10px}
.event .hl{color:var(--teal)}
.event em{color:var(--teal);font-size:10px}

/* footer */
.footer{left:128px;top:1224px;width:920px;height:252px;background:linear-gradient(#2a3030,#3b4242 70%,#2c3232);border-top:3px solid #1c2020}
.footer-strip{left:128px;top:1466px;width:920px;height:10px;background:var(--green-light)}
.f-title{position:absolute;font-size:11px;letter-spacing:.6px;color:#5fc0b6;padding-bottom:5px;border-bottom:1px solid #4a5252}
.sitemap{position:absolute;list-style:none;font-size:10.5px;color:#fff}
.sitemap li{height:21.8px}
.sitemap li::before{content:"›";color:#5fc0b6;margin-right:10px;font-size:13px}
.social{position:absolute;width:36px;height:36px;border-radius:50%;background:radial-gradient(circle at 40% 35%,#fff,#c9cccc);box-shadow:0 1px 3px rgba(0,0,0,.5)}
.copy{left:465px;top:1401px;font-size:10.5px;color:#ddd;letter-spacing:.4px}
.copy span{color:#5fc0b6}
.flabel{position:absolute;left:778px;font-size:10.5px;color:#fff}
.finput{position:absolute;left:824px;width:190px;background:#1f2424;border:1px solid #4a5252}
.go{left:826px;top:1402px;width:55px;height:25px;background:var(--green-light);color:#fff;font-size:11px;text-align:center;line-height:25px;border:1px solid #2a4a45}
</style>
</head>
<body>
<div class="stage">
  <div class="sheet"></div>

  <nav class="abs topnav">
    <a class="current" style="left:35px">Home</a>
    <a style="left:135px">About Us</a>
    <a style="left:251px">Associates</a>
    <a style="left:378px">Services</a>
    <a style="left:488px">Our Mission</a>
    <a style="left:621px">Contact</a>
    <div class="search">Search Site...</div>
  </nav>

  <div class="abs band"></div>
  <div class="abs brand">VELMORFIELD<br>FINANCIAL, INC.</div>
  <div class="abs tagline narrow">ALWAYS DO RIGHT THIS WILL GRATIFY SOME &amp; ASTONISH THE REST</div>

  <div class="abs callbox">
    <div class="cta narrow">CALL FOR A FREE CONSULTATION!</div>
    <div class="phone narrow">303-418-7639</div>
    <div class="login narrow" style="left:18px">Bluvexa Account Login</div>
    <div class="login narrow" style="left:160px">Quillbrook Account Login</div>
  </div>

  <div class="abs hero" role="img" aria-label="Businessman in a blue shirt beside an open road under a cloudy sky"></div>
  <div class="abs hero-card">
    <h1 class="narrow">Your guide on the road<br>to Financial Success</h1>
    <p class="narrow">Lorem ipsum dolor sit amet, consectetur adipiscing elit. Praesent dolor nunc, rhoncus porttitor bibendum</p>
    <div class="hero-btn narrow">CONTACT US FOR A FREE CONSULTATION</div>
  </div>

  <div class="abs intro-bar"></div>
  <section class="intro">
    <h2 class="narrow">LOREM IPSUM DOLOR SIT AMET, CONSECTETUR ADIPISCING ELI</h2>
    <p>Vestibulum vestibulum ante at lorem feugiat congue. Aenean elit tellus, dignissim at ege eu, <a>lobortis tincidunt</a> diam. Pellentesque vulputate elit sed nibh dapibus volutpat. Phase llus risus magna, pharetra quis venenatis in, tincidunt ac ipsum errerting oller ontandtise.</p>
    <div class="more-link">FIND OUT MORE &gt;</div>
  </section>

  <div class="abs news-box">
    <div class="head narrow">Sign up to our Newsletter</div>
    <div class="field" style="top:38px">Your Name</div>
    <div class="field" style="top:69px">Your Email</div>
    <div class="btn" style="left:84px;top:103px;width:62px">Submit</div>
  </div>

  <div class="abs dots" style="top:658px"></div>

  <div class="card" style="left:164px">
    <div class="head narrow">Investment Advice and Education</div>
    <div class="pic" role="img" aria-label="Tax forms and a pen on a desk" style="background:linear-gradient(135deg,#e8ecee,#9fb4c4)"></div>
    <h3>Lorem ipsum dolor sit amet</h3>
    <p>consectetur adipiscing elit. Sus-<br>pendisse id magna sem. Ut non<br>vulputate tortor poerting don.</p>
    <div class="btn">Submit</div>
  </div>
  <div class="card" style="left:379px">
    <div class="head narrow">Investment Advice and Education</div>
    <div class="pic" role="img" aria-label="Business team meeting around a table" style="background:linear-gradient(135deg,#d8d2c8,#5a5550)"></div>
    <h3>Lorem ipsum dolor sit amet</h3>
    <p>consectetur adipiscing elit. Sus-<br>pendisse id magna sem. Ut non<br>vulputate tortor poerting don.</p>
    <div class="btn">Submit</div>
  </div>
  <div class="card" style="left:594px">
    <div class="head narrow">Investment Advice and Education</div>
    <div class="pic" role="img" aria-label="Stack of paper files in an office" style="background:linear-gradient(180deg,#3a4346,#b9b6ad)"></div>
    <h3>Lorem ipsum dolor sit amet</h3>
    <p>consectetur adipiscing elit. Sus-<br>pendisse id magna sem. Ut non<br>vulputate tortor poerting don.</p>
    <div class="btn">Submit</div>
  </div>
  <div class="card" style="left:809px">
    <div class="head narrow">Investment Advice and Education</div>
    <div class="pic" role="img" aria-label="Advisors working with a laptop and phone" style="background:linear-gradient(135deg,#dfe3e0,#8d9a94)"></div>
    <h3>Lorem ipsum dolor sit amet</h3>
    <p>consectetur adipiscing elit. Sus-<br>pendisse id magna sem. Ut non<br>vulputate tortor poerting don.</p>
    <div class="btn">Submit</div>
  </div>

  <div class="abs dots" style="top:960px"></div>

  <div class="col-title narrow" style="left:164px;top:980px">LATEST NEWS</div>
  <div class="news" style="top:1011px;height:82px">
    <a>News headline will go here</a>
    <div class="date">12th October 2012</div>
    Phasellus risus magna, pharetra quis venena-<br>tis in, tincidunt ac ips... &nbsp;<em>more</em>
  </div>
  <div class="news" style="top:1099px;height:81px">
    <a>News headline will go here</a>
    <div class="date">12th October 2012</div>
    Phasellus risus magna, pharetra quis venena-<br>tis in, tincidunt ac ips... &nbsp;<em>more</em>
  </div>

  <div class="col-title narrow" style="left:459px;top:982px">QUICK LINKS</div>
  <ul class="qlinks">
    <li><svg width="10" height="12" viewBox="0 0 10 12"><path d="M2 1l6 5-6 5" fill="none" stroke="#aaa" stroke-width="2"/></svg><a>Our Firm</a></li>
    <li><svg width="10" height="12" viewBox="0 0 10 12"><path d="M2 1l6 5-6 5" fill="none" stroke="#aaa" stroke-width="2"/></svg><a>Our Associates</a></li>
    <li><svg width="10" height="12" viewBox="0 0 10 12"><path d="M2 1l6 5-6 5" fill="none" stroke="#aaa" stroke-width="2"/></svg><a>Our Location</a></li>
    <li><svg width="10" height="12" viewBox="0 0 10 12"><path d="M2 1l6 5-6 5" fill="none" stroke="#aaa" stroke-width="2"/></svg><a>Our Services</a></li>
    <li><svg width="10" height="12" viewBox="0 0 10 12"><path d="M2 1l6 5-6 5" fill="none" stroke="#aaa" stroke-width="2"/></svg><a>Our Qualifications</a></li>
    <li><svg width="10" height="12" viewBox="0 0 10 12"><path d="M2 1l6 5-6 5" fill="none" stroke="#aaa" stroke-width="2"/></svg><a>Our Articles</a></li>
  </ul>

  <div class="col-title narrow" style="left:751px;top:982px">EVENT LISTING</div>
  <div class="event" style="top:1019px">
    <div class="thumb" role="img" aria-label="Presenter at a whiteboard" style="background:linear-gradient(135deg,#eef0f0,#9aa4a8)"></div>
    <div class="txt"><span class="d">12th January 2013</span><br>Phasellus risus magna, phare-<br>tra quis venenatis in, tincidunt<br><span class="hl">ac ipseler tiny fereding set</span><br><em>more</em></div>
  </div>
  <div class="event" style="top:1120px">
    <div class="thumb" role="img" aria-label="Pen signing a document" style="background:linear-gradient(135deg,#f2f4f5,#8fb0c4)"></div>
    <div class="txt"><span class="d">12th October 2012</span><br>Phasellus risus magna, phare-<br>tra quis venenatis in, tincidunt<br>ac ipseler tiny fereding set<br><em>more</em></div>
  </div>

  <footer>
    <div class="abs footer"></div>
    <div class="abs footer-strip"></div>
    <div class="f-title" style="left:164px;top:1264px;width:242px">SITEMAP</div>
    <ul class="sitemap" style="left:172px;top:1291px">
      <li>Guidance &amp; Resources</li><li>Publications</li><li>Training</li><li>Peer Exchange</li><li>Certifications</li><li>Governance</li>
    </ul>
    <ul class="sitemap" style="left:312px;top:1291px">
      <li>About Us</li><li>Media</li><li>Membership</li><li>Not a member?</li><li>Login</li><li>Contact</li>
    </ul>
    <div class="f-title" style="left:467px;top:1264px;width:245px">FOLLOW US</div>
    <div class="social" aria-label="Social link" style="left:489px;top:1301px"></div>
    <div class="social" aria-label="Social link" style="left:568px;top:1301px"></div>
    <div class="social" aria-label="Social link" style="left:645px;top:1301px"></div>
    <div class="social" aria-label="Social link" style="left:489px;top:1348px"></div>
    <div class="social" aria-label="Social link" style="left:568px;top:1348px"></div>
    <div class="social" aria-label="Social link" style="left:645px;top:1348px"></div>
    <div class="abs copy">© Copyright <span>business</span> 2013 &nbsp;| &nbsp;All rights reserved</div>

    <div class="f-title" style="left:777px;top:1263px;width:238px">CONTACT US</div>
    <div class="flabel" style="top:1297px">Name</div>
    <div class="finput" style="top:1291px;height:24px"></div>
    <div class="flabel" style="top:1324px">Email</div>
    <div class="finput" style="top:1319px;height:24px"></div>
    <div class="flabel" style="top:1351px">Message</div>
    <div class="finput" style="top:1348px;height:47px"></div>
    <div class="abs go">GO</div>
  </footer>
</div>
</body>
</html>
```